Business Cards

Need a neat design for a new business card

Industry/Entity Type

Residential Construction

Contact Information for Business Card

Company Name- KOVE Construction Inc.
Owner- Marcus Tolliver
Phone number- (555)203-7481
Email- kovecohomes@brindlemail.example
Facebook- www.socialpage.example/kovecohomes

Colors
fefdec

```html
<!DOCTYPE html>
<html lang="en">
<head>
<meta charset="utf-8">
<title>KOVE Construction Inc. – Business Cards</title>
<link rel="stylesheet" href="https://fonts.googleapis.com/css2?family=Josefin+Sans:wght@300;400;600&display=swap">
<style>
  :root {
    --backdrop: #2a2522;
    --card: #1d1d1d;
    --ink: #fefdec;
    --ink-soft: #c9c8ba;
    --rule: #8a8a80;
  }
  * { margin: 0; padding: 0; box-sizing: border-box; }
  html, body { width: 1200px; height: 1008px; overflow: hidden; }
  body {
    background: var(--backdrop);
    font-family: "Josefin Sans", sans-serif;
    color: var(--ink);
    position: relative;
  }
  .card {
    position: absolute;
    left: 250px;
    width: 700px;
    height: 400px;
    background: var(--card);
    border-radius: 4px;
    box-shadow: 0 10px 30px rgba(0,0,0,0.45);
  }
  .card--front { top: 84px; }
  .card--back { top: 524px; }

  /* Front */
  .front-brand {
    position: absolute;
    inset: 0;
    display: flex;
    align-items: center;
    justify-content: center;
    gap: 18px;
  }
  .brand-mark {
    width: 22px;
    height: 22px;
    background: var(--ink);
  }
  .brand-name {
    font-weight: 400;
    font-size: 44px;
    letter-spacing: 4px;
    color: var(--ink);
    line-height: 1;
  }

  /* Back */
  .back-brand {
    position: absolute;
    left: 48px;
    top: 120px;
    display: flex;
    align-items: center;
    gap: 12px;
  }
  .back-brand .brand-mark { width: 14px; height: 14px; }
  .back-brand .brand-name { font-size: 30px; letter-spacing: 3px; }

  .contact {
    position: absolute;
    left: 340px;
    top: 168px;
  }
  .contact__name {
    font-weight: 600;
    font-size: 22px;
    letter-spacing: 0.5px;
  }
  .contact__role {
    font-weight: 300;
    font-size: 14px;
    color: var(--ink-soft);
    margin-top: 4px;
  }
  .contact__rule {
    width: 44px;
    height: 1px;
    background: var(--rule);
    margin: 12px 0 14px;
  }
  .contact__list { list-style: none; }
  .contact__item {
    display: flex;
    align-items: center;
    gap: 10px;
    font-weight: 300;
    font-size: 15px;
    line-height: 26px;
  }
  .contact__icon { width: 13px; height: 13px; flex: none; }
</style>
</head>
<body>

<section class="card card--front" aria-label="Business card front">
  <div class="front-brand">
    <span class="brand-mark"></span>
    <span class="brand-name">KOVE CONSTRUCTION</span>
  </div>
</section>

<section class="card card--back" aria-label="Business card back">
  <div class="back-brand">
    <span class="brand-mark"></span>
    <span class="brand-name">KOVE</span>
  </div>

  <div class="contact">
    <div class="contact__name">Marcus Tolliver</div>
    <div class="contact__role">Owner</div>
    <div class="contact__rule"></div>
    <ul class="contact__list">
      <li class="contact__item">
        <svg class="contact__icon" viewBox="0 0 16 16" aria-hidden="true">
          <path fill="var(--ink)" d="M3.6 1.2l2.3 2.6-1.3 1.8c.9 2 2.2 3.4 4.2 4.3l1.8-1.3 2.6 2.3-1.3 2.3C6.4 15 1 9.6 1.3 2.5z"/>
        </svg>
        <span>(555)203-7481</span>
      </li>
      <li class="contact__item">
        <svg class="contact__icon" viewBox="0 0 16 16" aria-hidden="true">
          <rect x="1" y="3" width="14" height="10" rx="1" fill="var(--ink)"/>
          <path d="M1.5 3.8L8 9l6.5-5.2" stroke="var(--card)" stroke-width="1.4" fill="none"/>
        </svg>
        <span>kovecohomes@brindlemail.example</span>
      </li>
      <li class="contact__item">
        <svg class="contact__icon" viewBox="0 0 16 16" aria-hidden="true">
          <rect x="1" y="1" width="14" height="14" rx="2" fill="var(--ink)"/>
        </svg>
        <span>www.socialpage.example/kovecohomes</span>
      </li>
    </ul>
  </div>
</section>

</body>
</html>
```